Crestline Gas and Plumbing Business Card Design

I am after a business card design for my plumbing business called 'Crestline Gas & Plumbing'. I do all types of plumbing and gas work and specialise in general maintenance plumbing. Would like to see designs using current logo

Industry/Entity Type

Plumbing

Contact Information for Business Card

Name - Dale Whitcombe
Phone number - 0455163027
Email - admin@crestlinegasandplumbing.example.com.au
ABN - 68204915336

```html
<!DOCTYPE html>
<html lang="en">
<head>
<meta charset="utf-8">
<title>Crestline Gas &amp; Plumbing – Business Card</title>
<link rel="stylesheet" href="https://fonts.googleapis.com/css2?family=Montserrat:wght@700;800&family=Lato:wght@400&display=swap">
<style>
  :root {
    --backdrop: #262626;
    --card-front: #1c1c1c;
    --card-back: #ececef;
    --brand-blue: #1f5cb8;
    --brand-orange: #f39320;
    --text-grey: #555559;
    --rule-grey: #b9b9bd;
  }
  * { margin: 0; padding: 0; box-sizing: border-box; }
  html, body {
    width: 1200px; height: 1200px; overflow: hidden;
    background: var(--backdrop);
  }
  .canvas { position: relative; width: 1200px; height: 1200px; }

  .card { position: absolute; left: 185px; width: 830px; box-shadow: 0 8px 24px rgba(0,0,0,.45); }
  .card--front { top: 86px; height: 474px; background: var(--card-front); }
  .card--back  { top: 640px; height: 466px; background: var(--card-back); }

  /* Front: centred brand name */
  .front-brand {
    position: absolute; inset: 0;
    display: flex; align-items: center; justify-content: center; gap: 18px;
  }
  .brand-dot { width: 34px; height: 34px; border-radius: 50%; background: var(--brand-orange); }
  .front-brand__name {
    font-family: "Montserrat", sans-serif; font-weight: 800;
    font-size: 30px; letter-spacing: 1px; color: #ffffff; text-transform: uppercase;
    line-height: 1.15;
  }

  /* Back: brand block */
  .back-brand {
    position: absolute; left: 66px; top: 196px; width: 326px;
    font-family: "Montserrat", sans-serif; font-weight: 800; color: var(--brand-blue);
    text-transform: uppercase;
  }
  .back-brand__name { font-size: 38px; line-height: 1; letter-spacing: -0.5px; }
  .back-brand__trade { font-size: 15px; letter-spacing: 1.5px; margin-top: 6px; }

  .divider {
    position: absolute; left: 413px; top: 148px; width: 1px; height: 166px;
    background: var(--rule-grey);
  }

  .contact { position: absolute; left: 427px; top: 140px; }
  .contact__name {
    font-family: "Montserrat", sans-serif; font-weight: 700;
    font-size: 28px; color: var(--brand-blue); text-transform: uppercase; line-height: 1.1;
  }
  .contact__role {
    font-family: "Lato", sans-serif; font-size: 25px; color: var(--brand-orange); line-height: 1.2;
  }
  .contact__abn {
    font-family: "Lato", sans-serif; font-size: 19px; color: var(--text-grey); margin-top: 22px;
  }
  .contact__abn .label { color: var(--brand-blue); }
  .contact__list { list-style: none; margin-top: 22px; }
  .contact__item {
    display: flex; align-items: center; gap: 8px;
    font-family: "Lato", sans-serif; color: var(--text-grey); line-height: 1.45;
  }
  .contact__item--phone { font-size: 19px; }
  .contact__item--email { font-size: 16px; }
  .contact__item svg { width: 13px; height: 13px; flex: none; }
</style>
</head>
<body>
<main class="canvas">
  <section class="card card--front" aria-label="Card front">
    <div class="front-brand">
      <span class="brand-dot"></span>
      <span class="front-brand__name">Crestline<br>Gas &amp; Plumbing</span>
    </div>
  </section>

  <section class="card card--back" aria-label="Card back">
    <div class="back-brand">
      <div class="back-brand__name">Crestline</div>
      <div class="back-brand__trade">Gas &amp; Plumbing</div>
    </div>

    <div class="divider"></div>

    <div class="contact">
      <h1 class="contact__name">Dale Whitcombe</h1>
      <p class="contact__role">Owner</p>
      <p class="contact__abn"><span class="label">ABN</span> - 68204915336</p>
      <ul class="contact__list">
        <li class="contact__item contact__item--phone">
          <svg viewBox="0 0 24 24" aria-hidden="true"><path fill="#f39320" d="M6.6 10.8a15.1 15.1 0 0 0 6.6 6.6l2.2-2.2c.3-.3.7-.4 1-.2 1.1.4 2.3.6 3.6.6.6 0 1 .4 1 1V20c0 .6-.4 1-1 1A17 17 0 0 1 3 4c0-.6.4-1 1-1h3.5c.6 0 1 .4 1 1 0 1.3.2 2.5.6 3.6.1.3 0 .7-.2 1z"/></svg>
          0455163027
        </li>
        <li class="contact__item contact__item--email">
          <svg viewBox="0 0 24 24" aria-hidden="true"><rect x="2" y="5" width="20" height="14" rx="1" fill="#f39320"/><path d="M2 6l10 7 10-7" fill="none" stroke="#fff" stroke-width="1.6"/></svg>
          admin@crestlinegasandplumbing.example.com.au
        </li>
      </ul>
    </div>
  </section>
</main>
</body>
</html>
```